Brightwater Health Partners, LLC Business Card update!

would like a classier business card. Our cards currently just have our logo and contact information. Need better use of color and creativity
Logo attached.

Target Market(s)

Potential clients, contacts, existing clients. We are a consulting company

Industry/Entity Type

Business

Contact Information for Business Card

We like our colors but just have a boring card with our logo and a white background. I want something that stands out.

Colors
ec1f27
757575

Requirements
Must have
• Color to stay consistent. Logo provided
Nice to have
• Just better use of color/ design

```html
<!DOCTYPE html>
<html lang="en">
<head>
<meta charset="utf-8">
<title>Brightwater Health Partners – Business Card</title>
<link rel="stylesheet" href="https://fonts.googleapis.com/css2?family=Open+Sans:wght@400;700&display=swap">
<style>
  :root {
    --brand-red: #ec1f27;
    --brand-grey: #757575;
    --card-white: #f4f4f4;
    --tint-pink: #f6e3e4;
    --tint-grey: #e6e6e6;
    --backdrop: #3a3a3a;
  }
  * { box-sizing: border-box; margin: 0; padding: 0; }
  html, body {
    width: 1200px;
    height: 900px;
    overflow: hidden;
  }
  body {
    background: var(--backdrop);
    display: flex;
    align-items: center;
    justify-content: center;
    font-family: "Open Sans", Arial, sans-serif;
  }
  .business-card {
    position: relative;
    width: 840px;
    height: 480px;
    background: var(--card-white);
    border-radius: 6px;
    overflow: hidden;
    box-shadow: 0 20px 50px rgba(0,0,0,0.45);
  }
  .accent-tint {
    position: absolute;
    top: 0;
    right: 0;
    width: 430px;
    height: 100%;
    background: linear-gradient(120deg, rgba(246,227,228,0) 0%, var(--tint-pink) 55%, var(--tint-grey) 100%);
    opacity: 0.75;
  }
  .brand {
    position: absolute;
    top: 92px;
    left: 60px;
    display: flex;
    align-items: center;
    gap: 18px;
  }
  .brand-mark {
    width: 56px;
    height: 56px;
    border-radius: 50%;
    background: var(--brand-red);
    flex: none;
  }
  .brand-name {
    color: var(--brand-red);
    font-size: 36px;
    font-weight: 400;
    letter-spacing: 0.5px;
    line-height: 1;
  }
  .contact {
    position: absolute;
    top: 196px;
    left: 134px;
    color: var(--brand-grey);
  }
  .contact-name {
    font-size: 32px;
    font-weight: 700;
    letter-spacing: 1px;
    margin-bottom: 8px;
  }
  .contact-line {
    font-size: 25px;
    font-weight: 400;
    line-height: 1.42;
  }
</style>
</head>
<body>
  <div class="business-card">
    <div class="accent-tint"></div>
    <div class="brand">
      <div class="brand-mark"></div>
      <div class="brand-name">Brightwater Health Partners</div>
    </div>
    <div class="contact">
      <div class="contact-name">LENA VAREK</div>
      <div class="contact-line">Harbor Lane 48</div>
      <div class="contact-line">5550102030</div>
      <div class="contact-line">lenavarek@brightwaterhealth.com</div>
      <div class="contact-line">www.brightwaterhealth.com</div>
    </div>
  </div>
</body>
</html>
```